Growing Tree Care company looking for 1st Van Wrap Design to build our fleet

We are a tree care company in the Twin Cities, MN market which offer Plant Health Care service to treat trees for disease, insect and provide nutrients to help grow healthy trees. We have added our first Delmor Vanta Van to the fleet which our tech will drive up to 20 plus homes and properties to apply treatments. We would like a uniquely branded wrap to catch the eye of potential clients leaving them with a lasting impression about who we are and what we do.

Target Market(s)

Homeowners that value the health of their trees

Other font styles liked:
• MONTSERRAT

Requirements
Must have
• company logo, brand font and brand colors (see files attached) Van is white.

```html
<!DOCTYPE html>
<html lang="en">
<head>
<meta charset="utf-8">
<title>Alder Tree Care — Delmor Vanta Van Wrap</title>
<link href="https://fonts.googleapis.com/css2?family=Montserrat:wght@500;600;700&display=swap" rel="stylesheet">
<style>
  :root{
    --brand-red:#c8182b;
    --brand-red-deep:#8a0d1b;
    --brand-red-light:#e0473f;
    --wrap-white:#ffffff;
    --trim-grey:#666666;
    --trim-grey-dark:#4d4d4d;
    --glass:#e4e4e4;
    --tyre:#0f0f0f;
    --rim:#d6d6d6;
    --page:#ffffff;
  }
  html,body{margin:0;padding:0;overflow:hidden;background:var(--page);}
  .sheet{width:1200px;height:782px;overflow:hidden;}
  .sheet svg{display:block;width:1200px;height:782px;}
  .wordmark{font-family:"Montserrat",sans-serif;font-weight:700;fill:var(--wrap-white);}
  .tagline{font-family:"Montserrat",sans-serif;font-weight:600;fill:var(--wrap-white);}
  .contact{font-family:"Montserrat",sans-serif;font-weight:700;fill:var(--brand-red);}
  .contact-light{font-family:"Montserrat",sans-serif;font-weight:600;fill:var(--wrap-white);}
  .body-red{fill:url(#redShade);}
  .body-white{fill:var(--wrap-white);}
  .trim{fill:var(--trim-grey);}
  .arch{fill:var(--trim-grey-dark);}
  .glass{fill:var(--glass);stroke:#9a9a9a;stroke-width:2;}
  .tyre{fill:var(--tyre);}
  .rim{fill:var(--rim);stroke:#888;stroke-width:2;}
  .hub{fill:#9a9a9a;}
  .tail-light{fill:#e8343a;}
  .tree-art{fill:url(#treeShade);}
  .swoosh{fill:none;stroke:var(--brand-red-light);stroke-width:5;}
  .logo-dot{fill:var(--wrap-white);}
</style>
</head>
<body>
<div class="sheet">
<svg viewBox="0 0 1500 978" preserveAspectRatio="none" xmlns="http://www.w3.org/2000/svg">
  <defs>
    <linearGradient id="redShade" x1="0" y1="0" x2="0" y2="1">
      <stop offset="0" stop-color="#8a0d1b"/>
      <stop offset="1" stop-color="#cc1c2f"/>
    </linearGradient>
    <radialGradient id="treeShade" cx="0.5" cy="0.45" r="0.55">
      <stop offset="0" stop-color="#9e1221" stop-opacity="0.9"/>
      <stop offset="1" stop-color="#9e1221" stop-opacity="0"/>
    </radialGradient>
    <linearGradient id="stripeFade" x1="0" y1="0" x2="1" y2="0">
      <stop offset="0" stop-color="#e0473f" stop-opacity="0.9"/>
      <stop offset="1" stop-color="#e0473f" stop-opacity="0.1"/>
    </linearGradient>
    <g id="vanSide">
      <path class="body-red" d="M58,300 Q150,268 215,250 L330,110 Q345,90 380,88 L838,88 Q852,92 855,115 L868,345 L58,352 Z"/>
      <path class="body-white" d="M215,305 Q520,225 868,262 L868,350 L215,352 Z"/>
      <path class="swoosh" stroke="url(#stripeFade)" d="M215,322 Q460,255 640,250"/>
      <path class="swoosh" stroke="url(#stripeFade)" d="M230,336 Q470,268 660,262"/>
      <path class="swoosh" stroke="url(#stripeFade)" d="M245,348 Q480,282 680,274"/>
      <polygon class="glass" points="218,286 282,186 352,180 352,272 285,280"/>
      <path class="glass" d="M80,300 Q120,285 150,280 L140,312 Q105,318 82,316 Z"/>
      <rect class="tail-light" x="832" y="262" width="20" height="84" rx="3"/>
      <path class="trim" d="M48,350 L878,345 L878,400 L48,405 Z"/>
      <circle class="arch" cx="195" cy="405" r="60"/>
      <circle class="arch" cx="710" cy="402" r="60"/>
      <circle class="tyre" cx="195" cy="412" r="48"/>
      <circle class="rim" cx="195" cy="412" r="34"/>
      <circle class="hub" cx="195" cy="412" r="9"/>
      <circle class="tyre" cx="710" cy="412" r="48"/>
      <circle class="rim" cx="710" cy="412" r="34"/>
      <circle class="hub" cx="710" cy="412" r="9"/>
      <ellipse class="tree-art" cx="430" cy="180" rx="100" ry="95" role="img" aria-label="Stylised leafy tree illustration in deep red"/>
    </g>
  </defs>

  <!-- Driver side (facing left) -->
  <g class="van van--left">
    <use href="#vanSide"/>
    <text class="wordmark" x="553" y="195" font-size="76">ALDER</text>
    <text class="tagline" x="612" y="238" font-size="33">Tree Care</text>
    <circle class="logo-dot" cx="793" cy="226" r="17"/>
    <text class="contact" x="570" y="300" font-size="22">Call:555 014 2290</text>
    <text class="contact" x="558" y="318" font-size="17">www.aldertreecare.com</text>
  </g>

  <!-- Passenger side (facing right) -->
  <g class="van van--right">
    <use href="#vanSide" transform="translate(926,430) scale(-1,1)"/>
    <text class="wordmark" x="138" y="625" font-size="76">ALDER</text>
    <text class="tagline" x="197" y="668" font-size="33">Tree Care</text>
    <circle class="logo-dot" cx="378" cy="657" r="17"/>
    <text class="contact" x="143" y="715" font-size="22">Call:555 014 2290</text>
    <text class="contact" x="130" y="734" font-size="17">www.aldertreecare.com</text>
  </g>

  <!-- Rear doors -->
  <g class="van van--rear">
    <rect x="968" y="408" width="28" height="46" rx="6" fill="#f2f2f2" stroke="#888" stroke-width="2"/>
    <rect x="1424" y="408" width="28" height="46" rx="6" fill="#f2f2f2" stroke="#888" stroke-width="2"/>
    <rect class="tyre" x="993" y="630" width="62" height="138" rx="10"/>
    <rect class="tyre" x="1363" y="630" width="62" height="138" rx="10"/>
    <path class="body-red" d="M1020,200 Q1030,185 1060,185 L1380,185 Q1408,185 1412,205 L1425,585 L1000,585 Z"/>
    <path class="body-white" d="M1022,470 Q1220,370 1418,382 L1425,585 L1000,585 Z"/>
    <path class="swoosh" stroke="url(#stripeFade)" d="M1025,482 Q1180,410 1320,392"/>
    <path class="swoosh" stroke="url(#stripeFade)" d="M1025,496 Q1170,425 1300,406"/>
    <line x1="1210" y1="195" x2="1210" y2="640" stroke="#5a0a12" stroke-width="2" opacity="0.6"/>
    <rect class="tail-light" x="995" y="445" width="26" height="135" rx="4"/>
    <rect class="tail-light" x="1398" y="445" width="26" height="135" rx="4"/>
    <path class="trim" d="M990,580 L1435,580 L1432,645 L993,645 Z"/>
    <ellipse class="tree-art" cx="1302" cy="490" rx="95" ry="95" role="img" aria-label="Stylised leafy tree illustration in red on the right door"/>
    <text class="wordmark" x="1053" y="338" font-size="44">ALDER</text>
    <text class="tagline" x="1087" y="362" font-size="19">Tree Care</text>
    <circle class="logo-dot" cx="1188" cy="355" r="10"/>
    <text class="contact-light" x="1232" y="330" font-size="17">+555 014 2290</text>
    <text class="contact-light" x="1216" y="348" font-size="17">aldertreecare.com</text>
  </g>
</svg>
</div>
</body>
</html>
```